Stationary Set Rebrand for Brenton

We are a Canadian Distribution and Service Company that was established in 1969. Over the past 5 decades we have expanded our business and have warehouses across Canada. We specialize in adhesive tapes, adhesives, films, safety, warehouse, shipping, janitorial and packaging supplies.

We have updated our logo design and would like a new corporate branding identity that includes a new fresh Stationary Set (Business Cards, Letterhead, Letterhead MS Word, Envelope, Presentation Folders, Email Signatures, Notepad Covers, etc.)

Target Market(s)

Industrial Business Sector

Font styles to use
Sans Serif

Colors
0054AA
0677BA
7BADD7
CADEEF
E8F1F8
0094D4
00A9DD
6FCCEA
C7EBF8
E9F6FB
00AB8E
00BBA5
67D7C9
C6EFE9
E9F9F6
EB3D1F
EC4F4E
F09395
F8D3D4
FCEDEE

Requirements
Should not have
• Colors not too light, darker colours preferred

```html
<!DOCTYPE html>
<html lang="en">
<head>
<meta charset="utf-8">
<title>Brenton Letterhead</title>
<link href="https://fonts.googleapis.com/css2?family=Bebas+Neue&family=Didact+Gothic&family=Roboto+Condensed:wght@700;900&display=swap" rel="stylesheet">
<style>
  :root {
    --stage: #4d4d4d;
    --paper: #ffffff;
    --ink: #000000;
    --accent: #ff0000;
    --accent-soft: #ff9999;
    --mist: #d1c6c6;
    --shadow: #4a4a4a;
  }
  * { margin: 0; padding: 0; box-sizing: border-box; }
  html, body { width: 1061px; height: 1200px; overflow: hidden; background: var(--stage); }
  .stage { position: relative; width: 1061px; height: 1200px; }
  .stage-title {
    position: absolute; top: 98px; left: 0; width: 100%;
    text-align: center; color: var(--paper);
    font-family: "Bebas Neue", sans-serif; font-weight: 400; font-size: 44px;
    line-height: 1;
  }
  .letterhead {
    position: absolute; left: 224px; top: 191px; width: 627px; height: 883px;
    background: var(--paper); overflow: hidden;
  }
  .brand { position: absolute; left: 81px; top: 50px; }
  .brand-name {
    font-family: "Roboto Condensed", sans-serif; font-weight: 900;
    font-size: 48px; line-height: 1; color: var(--ink); letter-spacing: -0.5px;
  }
  .brand-tagline {
    font-family: "Roboto Condensed", sans-serif; font-weight: 700;
    font-size: 11px; line-height: 1.2; color: var(--ink); margin-top: 2px;
  }
  .divider {
    position: absolute; left: 376px; top: 47px; width: 1px; height: 69px;
    background: var(--accent);
  }
  .contact {
    position: absolute; left: 399px; top: 45px; list-style: none;
    font-family: "Didact Gothic", sans-serif; font-size: 10.5px; color: var(--ink);
    line-height: 12.5px;
  }
  .contact li { display: flex; align-items: flex-start; }
  .contact .gap { margin-top: 6px; }
  .contact svg { width: 9px; height: 9px; flex: none; margin: 2px 2px 0 0; }
  .contact .indent { padding-left: 11px; }
  .footer-band {
    position: absolute; left: 0; bottom: 0; width: 627px; height: 120px;
    background: linear-gradient(90deg, var(--ink) 0%, var(--shadow) 30%, var(--mist) 55%, var(--accent) 78%, var(--accent-soft) 100%);
  }
</style>
</head>
<body>
<div class="stage">
  <h1 class="stage-title">Letter Head</h1>

  <section class="letterhead">
    <div class="brand">
      <div class="brand-name">Brenton</div>
      <div class="brand-tagline">Tape and Packaging Specialists</div>
    </div>

    <div class="divider"></div>

    <ul class="contact">
      <li>
        <svg viewBox="0 0 10 10" aria-hidden="true"><path d="M5 1 L9.5 5 H8.3 V9 H6 V6.5 H4 V9 H1.7 V5 H0.5 Z" fill="var(--accent)"/></svg>
        <span>Brenton Avenue, Address details</span>
      </li>
      <li class="indent"><span>Vancouver, Canada.</span></li>
      <li class="gap">
        <svg viewBox="0 0 10 10" aria-hidden="true"><circle cx="5" cy="5" r="4.4" fill="none" stroke="var(--accent)" stroke-width="0.8"/><path d="M3.4 2.8 L4.3 2.6 L4.8 3.9 L4.2 4.3 Q4.7 5.5 5.8 5.9 L6.2 5.3 L7.4 5.8 L7.2 6.7 Q5.6 7.4 4 5.8 Q2.7 4.3 3.4 2.8 Z" fill="var(--accent)"/></svg>
        <span>+1 (604) 555 0148</span>
      </li>
      <li>
        <svg viewBox="0 0 10 10" aria-hidden="true"><circle cx="5" cy="5" r="4.4" fill="none" stroke="var(--accent)" stroke-width="0.8"/><rect x="2.6" y="3.3" width="4.8" height="3.4" fill="var(--accent)"/><path d="M2.6 3.3 L5 5.2 L7.4 3.3" fill="none" stroke="var(--paper)" stroke-width="0.6"/></svg>
        <span>info@brenton.ca</span>
      </li>
      <li>
        <svg viewBox="0 0 10 10" aria-hidden="true"><g fill="none" stroke="var(--accent)" stroke-width="0.8"><circle cx="5" cy="5" r="4.2"/><ellipse cx="5" cy="5" rx="1.8" ry="4.2"/><path d="M0.8 5 H9.2 M1.5 2.8 H8.5 M1.5 7.2 H8.5"/></g></svg>
        <span>www.brenton.ca</span>
      </li>
    </ul>

    <div class="footer-band" role="img" aria-label="Decorative footer area in black, grey, red and pink brand tones"></div>
  </section>
</div>
</body>
</html>
```